Continuing Professional Development Seminars
Power Point Template
• 11 juin 2011 15:52 rubenqol
thanks Velmoro
• 9 juin 2011 11:07 Velmoro
congrats your first project :)
• 9 juin 2011 02:48 tkvolaris
rubenqol - can you please upload a new draft that has the following slides:
1 - The title slide from draft#15 (I think this might be exactly the same in all subsequent drafts)
2 - The content slide from draft#15
3 - The content slide from draft#66
4 - The content slide from draft#68
5 - The last slide from draft#69
6 - The last slide from draft#15
I would like to see both of the end slides in the same draft.
Thanks.
• 7 juin 2011 08:20 tkvolaris
Thank you to all the designers who have submitted designs to date. The quality of the work is outstanding and is making the decision difficult.
I am still considering ALL the designs and will probably make a final decision soon. However, the designs that seem to stand out at the moment include (in no particular order) draft#50/draft#72, draft#15 (and the variations), draft#62 and draft#54.
• 6 juin 2011 06:31 tkvolaris
Draft#15 – can you please make the following changes:
1. Replace the last slide with a variant of the first slide. This new slide should be the same as the first slide, but with the following changes:
• The colours of the main background graphic should be reversed – so that becomes a red graphic with a blue stipe (instead of a blue graphic with a red stripe).
• Change the text - “Welcome to our Presentation” to “Thank you”.
• Change the white text (location and date) to the contact details you currently have on the last slide.
2. Can we try three small variations to the header on the content slides? Firstly, can you make the line under the presentation header about an inch smaller (so that it doesn’t go all the way to the logo). Secondly, can you please do a variant that reverses the logo and the header title (so that the logo is on the right and the presentation title is on the left). Thirdly, can you try a variant that doesn’t have the presentation header at all – only the logo? I would prefer having a look at all three slides to see how it looks. Thanks.
• 2 juin 2011 06:02 tkvolaris
Some of the recent designs have been very good. I particularly like the very bold graphical styles on the front pages whilst I prefer the more minimalist approach to the content slides.
I know that I said previously to try using our logo as a background watermark. However, on second thoughts I don’t think it really works. The watermarks are OK on the first slides, but on the content slides it is very distracting.
So far, my favourite designs are draft#15 and drafts#25-26. However, many of the designs have things I like or don’t like. Specifically,
• Draft#25 and Draft #26 – These designs are very effective. A bold front page and simple content pages. I think we would need to lose the watermarks on the content pages, but otherwise, these designs are on the right track.
• Draft#23 – I like the footer design of each content slide. Very simple and elegant.
• Draft#15 – perhaps my favourite design so far. Good bold first slide. The content slides are also good – maybe a little too busy as the moment?
• Draft#9 and Draft#10 – The first slides in these designs are very good. I like the strong bold designs. The content pages don’t really work – too much graphical background and not enough white space for content. One thing I like about these designs is the reverse colours of the background on the final slides.
Some of the other designs have similar good and bad points. However, I think I would be repeating myself if I discussed each one.
In summary, I like the first slides that are bold and emphasise our brand. The content slides should be simple, elegant and consistent.
• 31 mai 2011 19:56 tkvolaris
When I was looking through other projects on this website, there is one that I found that seems to be very effective. The project name is "Brisk Lanterns PowerPoint Template" and the design is draft#39.
I am not suggesting that I want a copy or a redraft of this design. It is just an example of something that I like.
• 31 mai 2011 19:47 tkvolaris
I like the designs that are creatively using the "swirls" on our logo. The first pages in draft#9 and draft#10 are interesting. I also didn't mind the first page in draft#11 (but note that it has been withdrawn?).
I think the logo needs to be more subtle on the content pages - maybe in the bottom right corner? Also maybe could use the logo as a watermark? Draft#4 uses a watermark, but being in the middle of the page, it might be a little distracting.

```html
<!DOCTYPE html>
<html lang="en">
<head>
<meta charset="utf-8">
<title>Seminar Presentation Template</title>
<link rel="stylesheet" href="https://fonts.googleapis.com/css2?family=Caladea:wght@400;700&family=Cinzel:wght@400;600&display=swap">
<style>
  :root {
    --stage: #121214;
    --slide-white: #ffffff;
    --mist: #dfe5ee;
    --brand-blue: #1c4aa0;
    --deep-blue: #17399a;
    --heading-blue: #1e73c4;
    --accent-red: #e0232a;
    --body-text: #3e3e3e;
    --muted-text: #555555;
  }
  * { margin: 0; padding: 0; box-sizing: border-box; }
  html, body { width: 1200px; height: 907px; overflow: hidden; background: var(--stage); }
  .deck { position: relative; width: 1200px; height: 907px; }
  .slide {
    position: absolute; width: 558px; height: 382px;
    background: var(--slide-white); overflow: hidden;
    font-family: "Caladea", Georgia, serif; color: var(--body-text);
  }
  .slide--title   { left: 30px;  top: 37px; }
  .slide--picture { left: 618px; top: 37px; }
  .slide--quote   { left: 30px;  top: 480px; }
  .slide--columns { left: 618px; top: 480px; }
  .slide-backdrop { position: absolute; inset: 0; width: 100%; height: 100%; }
  .brand-name {
    position: absolute; top: 14px; right: 22px;
    font-family: "Caladea", Georgia, serif; font-weight: 700;
    font-size: 22px; color: var(--deep-blue); letter-spacing: 0.5px;
  }
  .slide--title .brand-name { right: auto; left: 50%; transform: translateX(-50%); top: 18px; }
  .question-mark {
    position: absolute; left: 0; right: 0; top: 92px; text-align: center;
    font-family: "Caladea", Georgia, serif; font-size: 96px; line-height: 1; color: var(--brand-blue);
  }
  .question-text {
    position: absolute; left: 40px; right: 40px; top: 200px; text-align: center;
    font-family: "Cinzel", "Times New Roman", serif; font-size: 23px; line-height: 1.3; color: #2a2a2a;
  }
  .slide-heading {
    position: absolute; left: 26px; top: 26px;
    font-weight: 700; font-size: 21px; color: var(--heading-blue); letter-spacing: 0.3px;
  }
  .slide-heading .accent { color: var(--accent-red); }
  .picture-area {
    position: absolute; left: 25px; top: 70px; width: 302px; height: 168px;
    background: linear-gradient(160deg, #e9e6dc, #c9c4b6);
  }
  .picture-caption {
    position: absolute; left: 25px; width: 302px; top: 252px; text-align: center;
    font-size: 13px; color: var(--muted-text);
  }
  .side-text {
    position: absolute; left: 360px; width: 172px; top: 100px;
    font-size: 17px; line-height: 1.3; color: var(--body-text);
  }
  .quote-mark {
    position: absolute; font-family: "Caladea", Georgia, serif; font-weight: 700;
    font-size: 84px; line-height: 1; color: var(--brand-blue);
  }
  .quote-mark--open { left: 26px; top: 148px; }
  .quote-mark--close { right: 58px; top: 228px; }
  .quote-text {
    position: absolute; left: 80px; width: 400px; top: 170px;
    font-size: 17px; line-height: 1.3; color: var(--body-text);
  }
  .columns {
    position: absolute; left: 26px; right: 20px; top: 88px;
    display: grid; grid-template-columns: repeat(3, 1fr); column-gap: 26px;
  }
  .column-title { font-weight: 700; font-size: 17px; color: var(--heading-blue); margin-bottom: 4px; }
  .column-text { font-size: 14.5px; line-height: 1.28; color: var(--body-text); }
</style>
</head>
<body>
<main class="deck">

  <section class="slide slide--title">
    <svg class="slide-backdrop" viewBox="0 0 558 382" preserveAspectRatio="none" aria-hidden="true">
      <defs>
        <linearGradient id="mistTop1" x1="0" y1="0" x2="0" y2="1">
          <stop offset="0" stop-color="#d6dde8"/><stop offset="1" stop-color="#ffffff"/>
        </linearGradient>
      </defs>
      <path d="M0 0 H558 V58 Q279 90 0 58 Z" fill="url(#mistTop1)"/>
      <path d="M0 60 Q279 92 558 60" fill="none" stroke="#ffffff" stroke-width="3"/>
      <path d="M0 325 Q279 296 558 325" fill="none" stroke="var(--accent-red)" stroke-width="3"/>
      <path d="M0 338 Q279 312 558 338 V382 H0 Z" fill="var(--brand-blue)"/>
    </svg>
    <div class="brand-name">ARDEN</div>
    <div class="question-mark">?</div>
    <p class="question-text">How could the testimony be used<br>in a non-hearsay way?</p>
  </section>

  <section class="slide slide--picture">
    <svg class="slide-backdrop" viewBox="0 0 558 382" preserveAspectRatio="none" aria-hidden="true">
      <path d="M0 325 Q279 296 558 325" fill="none" stroke="var(--accent-red)" stroke-width="3"/>
      <path d="M0 338 Q279 312 558 338 V382 H0 Z" fill="var(--brand-blue)"/>
    </svg>
    <div class="brand-name">ARDEN</div>
    <h2 class="slide-heading">SAMPLES PICTURE AND <span class="accent">TEXT</span></h2>
    <div class="picture-area" role="img" aria-label="Sketched courtroom cartoon illustration"></div>
    <p class="picture-caption">Description in this line</p>
    <p class="side-text">Lorem ipsum dolor sit amet, consectetur adipiscing elit. Maecenas lobortis sollicitudin neque eget iaculis.</p>
  </section>

  <section class="slide slide--quote">
    <svg class="slide-backdrop" viewBox="0 0 558 382" preserveAspectRatio="none" aria-hidden="true">
      <defs>
        <linearGradient id="mistTop3" x1="0" y1="0" x2="0" y2="1">
          <stop offset="0" stop-color="#d6dde8"/><stop offset="1" stop-color="#ffffff"/>
        </linearGradient>
      </defs>
      <path d="M0 0 H558 V58 Q279 90 0 58 Z" fill="url(#mistTop3)"/>
      <path d="M0 325 Q279 296 558 325" fill="none" stroke="var(--accent-red)" stroke-width="3"/>
      <path d="M0 338 Q279 312 558 338 V382 H0 Z" fill="var(--brand-blue)"/>
    </svg>
    <div class="brand-name">ARDEN</div>
    <span class="quote-mark quote-mark--open">&ldquo;</span>
    <p class="quote-text">Lorem ipsum dolor sit amet, consectetur adipiscing elit. Maecenas lobortis sollicitudin neque eget iaculis.</p>
    <span class="quote-mark quote-mark--close">&rdquo;</span>
  </section>

  <section class="slide slide--columns">
    <svg class="slide-backdrop" viewBox="0 0 558 382" preserveAspectRatio="none" aria-hidden="true">
      <path d="M0 325 Q279 296 558 325" fill="none" stroke="var(--accent-red)" stroke-width="3"/>
      <path d="M0 338 Q279 312 558 338 V382 H0 Z" fill="var(--brand-blue)"/>
    </svg>
    <div class="brand-name">ARDEN</div>
    <h2 class="slide-heading">SAMPLES PICTURE AND <span class="accent">TEXT</span></h2>
    <div class="columns">
      <article>
        <h3 class="column-title">SAMPLES 1</h3>
        <p class="column-text">Lorem ipsum dolor sit amet, consectetur adipiscing elit. Maecenas lobortis sollicitudin neque eget iaculis.</p>
      </article>
      <article>
        <h3 class="column-title">SAMPLES 1</h3>
        <p class="column-text">Lorem ipsum dolor sit amet, consectetur adipiscing elit. Maecenas lobortis sollicitudin neque eget iaculis.</p>
      </article>
      <article>
        <h3 class="column-title">SAMPLES 1</h3>
        <p class="column-text">Lorem ipsum dolor sit amet, consectetur adipiscing elit. Maecenas lobortis sollicitudin neque eget iaculis.</p>
      </article>
    </div>
  </section>

</main>
</body>
</html>
```